Natural Health Supplement Company Needs a Product Label Designed

HARVEST ROOT LABS needs a PROBIOTICS product label designed.We are a natural health vitamin and dietary supplement company. Who ever wins will have the opportunity to design a lot more product labels for us.
Product name: PROBIOTICS
*Please use the attached logo and base the label text exactly off the Kelt Wellness label example.
Other product examples have been attached for inspiration.

Colors

Designer to choose colors to be used in the design.

Requirements
Must have
• Product name: PROBIOTICS
• *Please use the attached logo and base the label text exactly off the Kelt Wellness label example.
• Other product examples have been attached for inspiration.

```html
<!DOCTYPE html>
<html lang="en">
<head>
<meta charset="utf-8">
<title>Harvest Root Labs – Probiotics Label</title>
<link rel="stylesheet" href="https://fonts.googleapis.com/css2?family=Cinzel:wght@400;600&family=Open+Sans:wght@500;600&display=swap">
<style>
  :root {
    --page-bg: #f1f1f1;
    --silver-dark: #c9cccd;
    --silver-mid: #e4e6e7;
    --silver-light: #fbfbfb;
    --ink: #262626;
    --grey-text: #6b6b6b;
    --green: #6cc424;
    --green-light: #9be33a;
    --green-dark: #4a9a14;
    --hex-rim: #d9dcdc;
  }
  * { box-sizing: border-box; margin: 0; padding: 0; }
  html, body {
    width: 1200px; height: 1103px; overflow: hidden;
    background: var(--page-bg);
  }
  .label {
    position: absolute;
    left: 150px; top: 196px;
    width: 900px; height: 710px;
    background: linear-gradient(90deg,
      var(--silver-dark) 0%, var(--silver-mid) 14%, var(--silver-light) 30%,
      var(--silver-mid) 46%, var(--silver-light) 60%, var(--silver-mid) 80%,
      var(--silver-dark) 100%);
    border-top: 3px solid #b9bcbd;
    text-align: center;
    font-family: "Open Sans", sans-serif;
    color: var(--ink);
  }
  .brand {
    position: absolute; top: 120px; left: 0; right: 0;
    font-family: "Cinzel", serif; font-weight: 600;
    font-size: 54px; letter-spacing: 1px;
    color: var(--green);
  }
  .product-name {
    position: absolute; top: 228px; left: 0; right: 0;
    font-family: "Cinzel", serif; font-weight: 400;
    font-size: 96px; letter-spacing: 1px; color: var(--ink);
  }
  .grade {
    position: absolute; top: 366px; left: 95px; right: 95px;
    display: flex; align-items: center; gap: 16px;
    font-family: "Cinzel", serif; font-weight: 600;
    font-size: 28px; color: var(--grey-text);
  }
  .grade .rule { flex: 1; height: 3px; background: linear-gradient(90deg, transparent, #555 60%, #555); }
  .grade .rule.right { background: linear-gradient(90deg, #555, #555 40%, transparent); }
  .badges {
    position: absolute; top: 430px; left: 0; right: 0;
    display: flex; justify-content: center; gap: 58px;
  }
  .badge { position: relative; width: 150px; height: 160px; }
  .badge svg { position: absolute; inset: 0; }
  .badge-text {
    position: absolute; inset: 0;
    display: flex; flex-direction: column; align-items: center; justify-content: center;
    font-family: "Cinzel", serif; color: #fff; line-height: 1;
  }
  .badge-text .big { font-size: 54px; }
  .badge-text .small { font-size: 18px; margin-top: 6px; }
  .badge-text .mid { font-size: 24px; line-height: 1.05; }
  .tagline {
    position: absolute; top: 612px; left: 0; right: 0;
    font-size: 22px; font-weight: 500; color: var(--ink);
  }
  .band {
    position: absolute; left: 0; right: 0; bottom: -60px; height: 86px;
    background: linear-gradient(90deg, var(--green-dark), var(--green-light) 50%, var(--green));
    display: flex; align-items: center; justify-content: center; gap: 22px;
    font-size: 24px; font-weight: 600; color: #222;
  }
  .band .divider { width: 3px; height: 28px; background: #222; }
</style>
</head>
<body>
  <main class="label">
    <div class="brand">HARVEST ROOT LABS</div>
    <h1 class="product-name">PROBIOTICS</h1>
    <div class="grade"><span class="rule"></span>PREMIUM<span class="rule right"></span></div>

    <div class="badges">
      <div class="badge">
        <svg viewBox="0 0 150 160" width="150" height="160"><polygon points="75,4 144,42 144,118 75,156 6,118 6,42" fill="var(--hex-rim)"/><polygon points="75,12 137,46 137,114 75,148 13,114 13,46" fill="var(--green)"/></svg>
        <div class="badge-text"><span class="big">40</span><span class="small">BILLION</span><span class="small" style="margin-top:2px">CFU</span></div>
      </div>
      <div class="badge">
        <svg viewBox="0 0 150 160" width="150" height="160"><polygon points="75,4 144,42 144,118 75,156 6,118 6,42" fill="var(--hex-rim)"/><polygon points="75,12 137,46 137,114 75,148 13,114 13,46" fill="var(--green)"/></svg>
        <div class="badge-text"><span class="big">11</span><span class="small">STRAINS</span></div>
      </div>
      <div class="badge">
        <svg viewBox="0 0 150 160" width="150" height="160"><polygon points="75,4 144,42 144,118 75,156 6,118 6,42" fill="var(--hex-rim)"/><polygon points="75,12 137,46 137,114 75,148 13,114 13,46" fill="var(--green)"/></svg>
        <div class="badge-text"><span class="mid">ACID</span><span class="mid">&amp; BILE</span><span class="small" style="font-size:16px">RESISTANT</span></div>
      </div>
    </div>

    <p class="tagline">For Optimal Digestive and Immune Health</p>

    <div class="band"><span>DIETARY SUPPLEMENT</span><span class="divider"></span><span>30 CAPULES</span></div>
  </main>
</body>
</html>
```